Business acrd and Stationery desgin FOR DUNMORE

I want creative and expressive stationary design .on the front side for business card I need the logo and doctors name to be there and on the back side I need time and appointment .Please see attached business card to use same names ,but use address below and phone number

Note:the deigner must submit the file in vector format and PSD and PDF

Business name is :Dunmore Glen Medical Clinic.

Address:
20418 57 ST NW
City :EDMONTON AB
Postal code: T6K 3R8

Phone :(780) 555-0142
Fax:(780) 555-0187

Other Business name :Dunmore Medical Clinic

• logo in the back on business card

```html
<!DOCTYPE html>
<html lang="en">
<head>
<meta charset="utf-8">
<title>Dunmore Glen Medical Clinic – Business Card</title>
<link rel="stylesheet" href="https://fonts.googleapis.com/css2?family=Tinos:wght@400;700&display=swap">
<style>
  :root {
    --clinic-red: #ea1c24;
    --clinic-navy: #1f3f93;
    --paper-white: #ffffff;
    --blush: #f8bfa8;
    --ink-grey: #6e6e6e;
    --line-grey: #7d7d7d;
    --canvas-bg: #e4e5e7;
  }
  * { margin: 0; padding: 0; box-sizing: border-box; }
  html, body {
    width: 1200px; height: 1000px; overflow: hidden;
    background: var(--canvas-bg);
    font-family: "Tinos", "Times New Roman", serif;
  }
  .canvas { position: relative; width: 1200px; height: 1000px; }

  .card {
    position: absolute; left: 250px; width: 700px; height: 400px;
    overflow: hidden; box-shadow: 0 6px 18px rgba(0,0,0,0.18);
    background: var(--clinic-red);
  }
  .card--front { top: 50px; }
  .card--back { top: 540px; }

  /* Front */
  .front__header {
    position: absolute; left: 0; top: 0; width: 100%; height: 150px;
    background: var(--paper-white);
    display: flex; align-items: center; justify-content: center; gap: 22px;
    padding: 0 40px;
  }
  .brand-dot {
    width: 40px; height: 40px; border-radius: 50%; background: var(--clinic-red);
    flex: none;
  }
  .brand-name {
    color: var(--clinic-navy); font-weight: 400; font-size: 36px; line-height: 40px;
    letter-spacing: 1px; text-transform: uppercase; white-space: nowrap;
  }
  .front__pattern {
    position: absolute; left: 0; top: 150px; width: 100%; height: 110px;
    background: linear-gradient(180deg, rgba(255,255,255,0.14), rgba(255,255,255,0));
  }
  .front__capsules {
    position: absolute; left: 60px; top: 270px; width: 200px; height: 110px;
    border-radius: 8px;
    background: radial-gradient(ellipse at 50% 45%, rgba(255,240,235,0.85), rgba(255,210,205,0.25) 70%, rgba(234,28,36,0) 100%);
  }
  .front__details {
    position: absolute; right: 48px; top: 176px; text-align: right;
    color: var(--paper-white);
  }
  .doctor { font-size: 36px; line-height: 42px; letter-spacing: 0.5px; white-space: nowrap; }
  .address {
    margin-top: 12px; font-size: 16px; line-height: 21px; letter-spacing: 0.5px;
    font-style: normal; white-space: nowrap;
  }

  /* Back */
  .back__panel {
    position: absolute; left: 0; top: 40px; width: 100%; height: 290px;
    background: var(--blush);
  }
  .back__pattern {
    position: absolute; inset: 0;
    background: linear-gradient(90deg, rgba(255,255,255,0.2), rgba(255,255,255,0) 40%, rgba(255,255,255,0.15));
  }
  .back__brand {
    position: absolute; left: 60px; top: 20px;
    display: flex; align-items: center; gap: 8px;
  }
  .back__brand .brand-dot { width: 14px; height: 14px; }
  .back__brand .brand-name { font-size: 15px; line-height: 17px; letter-spacing: 0.5px; }
  .appointment-label {
    position: absolute; left: 58px; top: 90px;
    color: var(--ink-grey); font-size: 32px; line-height: 44px; letter-spacing: 1.5px;
  }
  .appointment-lines { position: absolute; left: 0; top: 0; width: 700px; height: 290px; }
  .back__capsules {
    position: absolute; right: 40px; top: 190px; width: 190px; height: 90px;
    border-radius: 8px;
    background: radial-gradient(ellipse at 55% 50%, rgba(255,255,255,0.85), rgba(255,230,222,0.3) 70%, rgba(248,191,168,0) 100%);
  }
</style>
</head>
<body>
<main class="canvas">

  <section class="card card--front" aria-label="Business card front">
    <header class="front__header">
      <span class="brand-dot"></span>
      <span class="brand-name">Dunmore Glen<br>Medical Clinic</span>
    </header>
    <div class="front__pattern" role="img" aria-label="Faint white wave line pattern"></div>
    <div class="front__capsules" role="img" aria-label="Photo of translucent medicine capsules"></div>
    <div class="front__details">
      <p class="doctor">Dr A Haddani</p>
      <p class="doctor">Dr Z Karimov</p>
      <address class="address">
        20418 57 ST NW<br>
        EDMONTON AB<br>
        T6K 3R8<br>
        Phone:(780) 555-0142<br>
        Fax:(780) 555-0187
      </address>
    </div>
  </section>

  <section class="card card--back" aria-label="Business card back">
    <div class="back__panel">
      <div class="back__pattern" role="img" aria-label="Faint white wave line pattern"></div>
      <div class="back__brand">
        <span class="brand-dot"></span>
        <span class="brand-name">Dunmore Medical<br>Clinic</span>
      </div>
      <p class="appointment-label">TIME<br>APPOINTMENT</p>
      <svg class="appointment-lines" viewBox="0 0 700 290" aria-hidden="true">
        <g stroke="var(--line-grey)" stroke-width="1.5">
          <line x1="330" y1="124" x2="640" y2="124"/>
          <line x1="330" y1="166" x2="640" y2="166"/>
          <line x1="60" y1="206" x2="640" y2="206"/>
        </g>
      </svg>
      <div class="back__capsules" role="img" aria-label="Photo of translucent medicine capsules"></div>
    </div>
  </section>

</main>
</body>
</html>
```